Two sided business card template for:

Room 4 Keeps Storage
1817 Brantley Avenue,
Saskatoon, SK
R3P 2W6
306-555-0184
www.room4keeps.ca

Front side should be standard business card information. Sample should be for Gregory Lindell, Operations Manager, greg@room4keeps.ca

Back side should be an advertisement for the storage facility. Some points about our facility are below you may use some or all of these features in the ad.

-Online payments and bookings
-Seasonal bicycle, tire, and motorcycle storage
-24hr self storage access
-Safe, and secure, with digital video surveillance
-Airport location

Card could have, but doesn't need a clever tag line containing the company name

Finished design must be in Microsoft word, or publisher format, and text must be editable.

```html
<!DOCTYPE html>
<html lang="en">
<head>
<meta charset="utf-8">
<title>Room 4 Keeps Storage – Business Card</title>
<link rel="stylesheet" href="https://fonts.googleapis.com/css2?family=Open+Sans:wght@400;600&display=swap">
<style>
  :root {
    --bg: #1e1e20;
    --blue-deep: #1669b8;
    --blue-light: #3f98df;
    --charcoal: #2a2a2c;
    --charcoal-dark: #1c1c1e;
    --white: #ffffff;
    --ink: #222222;
    --red: #d92b2b;
    --box-dark: #2b2b2b;
  }
  * { box-sizing: border-box; margin: 0; padding: 0; }
  html, body { width: 1200px; height: 800px; overflow: hidden; }
  body {
    background: var(--bg);
    font-family: "Open Sans", Arial, sans-serif;
    position: relative;
  }
  .card {
    position: absolute;
    width: 560px;
    height: 320px;
    overflow: hidden;
    box-shadow: 0 10px 30px rgba(0,0,0,0.45);
  }
  /* Back side: advertisement */
  .card--back {
    left: 80px; top: 70px;
    background: linear-gradient(135deg, var(--blue-deep) 0%, var(--blue-light) 60%, var(--blue-deep) 100%);
  }
  .brand-box {
    position: absolute;
    background: var(--white);
    display: flex; align-items: center; justify-content: center; gap: 10px;
  }
  .card--back .brand-box {
    left: 150px; top: 36px; width: 260px; height: 110px;
    border: 2px solid #111;
  }
  .brand-mark { width: 18px; height: 18px; background: var(--red); flex: none; }
  .brand-name {
    font-weight: 600; font-size: 20px; color: var(--ink);
    line-height: 1.1; letter-spacing: 0.2px;
  }
  .features {
    position: absolute; left: 150px; top: 168px;
    list-style: none; color: var(--white);
    font-size: 15px; line-height: 21px;
  }
  /* Front side: contact */
  .card--front {
    left: 560px; top: 410px;
    background: linear-gradient(135deg, var(--charcoal) 0%, var(--charcoal-dark) 100%);
  }
  .front-panel {
    position: absolute; left: 0; top: 0; width: 100%; height: 100%;
  }
  .card--front .brand-box {
    left: 322px; top: 70px; width: 210px; height: 124px;
  }
  .card--front .brand-name { font-size: 18px; }
  .contact {
    position: absolute; left: 28px; top: 20px; color: var(--white);
  }
  .contact__name { font-size: 19px; font-weight: 400; }
  .contact__title { font-size: 12px; color: var(--red); margin-top: 0; }
  .contact__box {
    margin-top: 8px; width: 178px;
    background: var(--box-dark);
    padding: 8px 10px; font-size: 13px; line-height: 26px;
  }
  .contact__address {
    margin-top: 12px; font-size: 13px; line-height: 27px; font-style: normal;
    padding-left: 8px;
  }
</style>
</head>
<body>

<section class="card card--back" aria-label="Card back: facility advertisement">
  <div class="brand-box">
    <span class="brand-mark"></span>
    <span class="brand-name">Room 4 Keeps<br>Storage</span>
  </div>
  <ul class="features">
    <li>Airport location</li>
    <li>24hr self storage access</li>
    <li>Online payments and bookings</li>
    <li>Seasonal bicycle, tire, and motorcycle storage</li>
    <li>Safe, and secure, with digital video surveillance</li>
  </ul>
</section>

<section class="card card--front" aria-label="Card front: contact details">
  <svg class="front-panel" viewBox="0 0 560 320" aria-hidden="true">
    <defs>
      <linearGradient id="frontBlue" x1="0" y1="0" x2="1" y2="1">
        <stop offset="0" stop-color="#1669b8"/>
        <stop offset="0.6" stop-color="#3f98df"/>
        <stop offset="1" stop-color="#1669b8"/>
      </linearGradient>
    </defs>
    <polygon points="0,0 262,0 300,320 0,320" fill="url(#frontBlue)"/>
    <polygon points="262,0 270,0 308,320 300,320" fill="#ffffff"/>
  </svg>
  <div class="contact">
    <p class="contact__name">Gregory Lindell</p>
    <p class="contact__title">Operations Manager</p>
    <div class="contact__box">
      <p>306-555-0184</p>
      <p>www.room4keeps.ca</p>
      <p>greg@room4keeps.ca</p>
    </div>
    <address class="contact__address">
      Room 4 Keeps Storage<br>
      1817 Brantley Avenue,<br>
      Saskatoon, SK<br>
      R3P 2W6
    </address>
  </div>
  <div class="brand-box">
    <span class="brand-mark"></span>
    <span class="brand-name">Room 4 Keeps<br>Storage</span>
  </div>
</section>

</body>
</html>
```